Veteran Owned General Contractor needs Bold New Business Cards

We are a service disabled veteran owned small business. We're a general contractor that specializes in excavation, underground utilities, site work, land clearing and demolition. We would like a fresh, simple, bold, new look for our business cards. We're open to ideas! We'd like to incorporate the following information on the card:

Company Name & Logo, Name of Person, Job Title, Office Phone, Fax, Cell Phone, Email Address, Website, SDVOSB

Our logo is included. We look forward to your thoughts.

Thank you!
Updates

Reason: Hello Due to the overwhelming response to this project, we are extending the deadline one time to allow for improved communication and feedback with the top candidates. We would like to thank everyone for their hard work and exceptional creativity! Thank you

Industry/Entity Type

Business

Contact Information for Business Card

Font styles to use
Sans Serif

Requirements
Nice to have
• As we are a veteran owned company, it would be nice to incorporate an American flag into the design. Maybe on the back?

```html
<!DOCTYPE html>
<html lang="en">
<head>
<meta charset="utf-8">
<title>Keystone 9 Inc. – Business Cards</title>
<link rel="stylesheet" href="https://fonts.googleapis.com/css2?family=Open+Sans:wght@400;600;800&family=Ubuntu:wght@300;400&display=swap">
<style>
  :root {
    --backdrop: #2b2b2b;
    --card: #1d1d1d;
    --green: #6cc04a;
    --grey: #8c8c8c;
    --white: #ffffff;
    --text-light: #e6e6e6;
  }
  * { box-sizing: border-box; margin: 0; padding: 0; }
  html, body { width: 1200px; height: 1000px; overflow: hidden; }
  body {
    background: var(--backdrop);
    font-family: "Open Sans", Arial, sans-serif;
    position: relative;
  }
  .card {
    position: absolute;
    left: 250px;
    width: 700px;
    height: 400px;
    background: var(--card);
    box-shadow: 0 10px 30px rgba(0,0,0,.45);
    overflow: hidden;
  }
  .card--back { top: 70px; }
  .card--front { top: 530px; }

  .brand {
    position: absolute;
    display: flex;
    align-items: center;
    gap: 18px;
    left: 50%;
    transform: translateX(-50%);
    white-space: nowrap;
  }
  .brand__square {
    width: 64px; height: 64px;
    background: var(--grey);
    border-radius: 6px;
  }
  .brand__name {
    font-weight: 800;
    font-size: 54px;
    letter-spacing: 2px;
    color: var(--green);
    line-height: 1;
  }
  .card--back .brand { top: 150px; }
  .card--front .brand { top: 55px; }

  .site-url {
    position: absolute;
    bottom: 38px;
    width: 100%;
    text-align: center;
    font-family: "Ubuntu", Arial, sans-serif;
    font-weight: 300;
    font-size: 15px;
    letter-spacing: 2px;
    color: var(--white);
  }
  .accent { color: var(--green); }

  .name-band {
    position: absolute;
    top: 180px;
    left: 0;
    width: 100%;
    height: 62px;
    background: var(--green);
    display: flex;
    align-items: center;
    justify-content: center;
    color: var(--white);
    font-weight: 600;
    font-size: 26px;
    letter-spacing: 2.5px;
  }

  .contact-list {
    position: absolute;
    left: 50px;
    top: 268px;
    list-style: none;
    font-family: "Ubuntu", Arial, sans-serif;
    font-weight: 300;
    font-size: 17px;
    color: var(--text-light);
    letter-spacing: 1px;
  }
  .contact-list li {
    display: flex;
    align-items: center;
    gap: 12px;
    height: 25px;
  }
  .contact-list svg { width: 15px; height: 15px; fill: var(--green); flex: none; }

  .address {
    position: absolute;
    right: 55px;
    top: 268px;
    text-align: right;
    font-family: "Ubuntu", Arial, sans-serif;
    font-weight: 300;
    font-size: 18px;
    line-height: 25px;
    color: var(--text-light);
    letter-spacing: .5px;
  }
  .address__company { color: var(--green); }
</style>
</head>
<body>

<section class="card card--back">
  <div class="brand">
    <span class="brand__square"></span>
    <span class="brand__name">KEYSTONE 9 INC</span>
  </div>
  <p class="site-url">www.<span class="accent">yoursitename</span>.com</p>
</section>

<section class="card card--front">
  <div class="brand">
    <span class="brand__square"></span>
    <span class="brand__name">KEYSTONE 9 INC</span>
  </div>

  <div class="name-band">DANIEL REYES - FOUNDER</div>

  <ul class="contact-list">
    <li>
      <svg viewBox="0 0 16 16" aria-hidden="true"><path d="M1 5c0-2 3-3 7-3s7 1 7 3v1.5h-3.5V5h-7v1.5H1zM3 8h10l1 6H2z"/></svg>
      000 000 0000
    </li>
    <li>
      <svg viewBox="0 0 16 16" aria-hidden="true"><path d="M3 1l3 0 1 4-2 1.5c1 2 2.5 3.5 4.5 4.5L11 9l4 1v3c0 1-1 2-2 2C7 15 1 9 1 3c0-1 1-2 2-2z"/></svg>
      000 000 0000
    </li>
    <li>
      <svg viewBox="0 0 16 16" aria-hidden="true"><path d="M4 1h6l2 2v4h2v8H2V7h2zM5 2v5h6V3.5L9.5 2zM4 9v2h2V9zm3 0v2h2V9zm3 0v2h2V9z"/></svg>
      000 000 0000
    </li>
    <li>
      <svg viewBox="0 0 16 16" aria-hidden="true"><path d="M1 3h14v1L8 9 1 4zM1 6l7 5 7-5v7H1z"/></svg>
      info@yourmail.com
    </li>
  </ul>

  <address class="address">
    <span class="address__company">Keystone 9 Inc.</span><br>
    your street address,<br>
    suite-123, country-1230<br>
    www.<span class="accent">yoursite</span>.com
  </address>
</section>

</body>
</html>
```